Coaching Business Needs a Website

Business Name: Bright Turn Mentoring
My Name: Marcus Pellingham

I am a human behaviour expert that needs not just a website, but in the process a "personality" for my brand (Bright Turn).

With your brilliance and creativity, I want my reputation to be the go to expert in changing unresourceful human behaviour (eg. smoking, eating sugar, procrastination, overwhelm, fear, laziness, weight-gain, phobias, lack of motivation, etc).

===========================
Page 1 (Titled: 'Start Here')

My tag line is "Bright Turn". The home page should be friendly, inviting, exciting, empowering, positive and innovative.

My Mission Quote: (so people know why I do what I do)

"Our mission is to improve as many people's lives as we can, when we can, through workshops, being guest speaker at events, coaching/mentoring and with valuable products." - Marcus Pellingham, Human Behaviour Expert (I will give you a photo of me to put with this quote).

My marketing strategy is to share how I ride, because that is my focus (the experience that clients get). Please show the following on my Page 1:

- My mission quote (see above).
- A video (please insert any video at this stage, as I will get a marketing video professionally made to go on this page 1 of my website).
- 10 Reasons Why People Choose 'Bright Turn Mentoring'.
- What We Offer (with Call To Action Buttons, see below).
- Success Stories (these are our Testimonials).

-------------------------------------------
10 Reasons Why People Choose 'Bright Turn Mentoring':

Reason No. 1 We know how to make Bright Turn in other people's lives. This is our favourite method of making change.

Reason No. 2 We give away a lot of FREE stuff.

Reason No. 3 We thank you for accepting FREE stuff. We are genuinely grateful for you accepting our FREE stuff.

Reason No. 4 We give you a feeling of belonging.

Reason No. 5 We give you the feeling that you are special, because you are.

Reason No. 6 We give you the feeling of significance, because you deserve it.

Reason No. 7 We give you the feeling of feeling good.

Reason No. 8 We give you positive, empowering experiences.

Reason No. 9 We give you tools, models and methodologies to improve every area of your life, continuously for the rest of your life. You can have fulfillment.

Reason No. 10 We give you value beyond what you can imagine.

What We Offer: (each of the following with a picture and more details)

1. Personal Coaching / Mentoring (more details: 1st Session FREE, valued at A$125, Unlimited chat support, call to action button to go to https://bookslotter.example/brightturnmentoring).

2. Human Behaviour Events (more details: next upcoming event, call to action button to go to... I will provide later.. I want to be able to change this hyperlink regularly to the latest upcoming event).

3. Guest Speaker / Master of Ceremonies (call to action button to go to 'Contact Us' website page).

4. Great Value Products (call to action button to go to 'Products' website page).

5. Great FREE Information (call to action button to go to 'Blogs' website page).

Success Stories:

Please allow for 10 written testimonial stories to be added. Please put 10 random text ones so I know what it will look like. I want to be able to change the text in the future. It would be good to put the person's picture and a star rating (eg. 5 stars).

Page 2 (Title: 'Products')

A place where I can add products...

Page 3 (Titled: 'Blogs')

A place where I can add written blogs...

Page 4 (Titled: 'Contact Us')

Contact us form with:
- Name
- Email Address
- Contact Number
- Message

Thank you. I look forward to working with you!!! I will upload my Logo for you to use.

Target Market(s)

Real, Everyday People - Men & Women aged between 21 - 50, who want to change several behaviours in their health, career, relationship, etc, that they feel are holding them back.

Industry/Entity Type

Life Coaching

Contact Information for Business Card

My Name: Marcus Pellingham, Bright Turn Expert
Mobile: xxxxxxxxxxxxxx
Email: xxxxxxxxxxxxxx@mailvane.example
Website: brightturnmentoring.example.au

On the back have what we do:
1. Personal Coaching / Mentoring
2. Human Behaviour Events
3. Guest Speaker / Master of Ceremonies

Coding

Coded - Design and coding required

Number of Pages Required

4 page

Colors
ffc214

Requirements
Must have
• Inspiring images... My website must come across as fun, social, happy, and inviting. The website must have a personality; it is a marketing lead generation tool. It must represent Marcus Pellingham as being a Human Behaviour Expert (ie. video & testimonials) and must have Call To Action buttons. The website should look professional, not something done using a cheap template. The colour selected is GOLD.
Nice to have
• Additional creative functionality...
Should not have
• It should not have anything negative on it.

```html
<!DOCTYPE html>
<html lang="en">
<head>
<meta charset="utf-8">
<title>Bright Turn Mentoring – Start Here</title>
<link href="https://fonts.googleapis.com/css2?family=Open+Sans+Condensed:wght@700&family=Open+Sans:wght@400;600;700&family=Mukta:wght@400;600&family=Dancing+Script:wght@600&display=swap" rel="stylesheet">
<style>
:root{
  --gold:#ffc214;
  --gold-deep:#f2ae00;
  --ink:#222222;
  --text:#3a3a3a;
  --muted:#6b6b6b;
  --paper:#ffffff;
  --mist:#efefef;
  --footer:#231f20;
}
*{box-sizing:border-box;margin:0;padding:0}
html,body{width:1200px;height:2897px;overflow:hidden}
body{position:relative;background:var(--paper);font-family:"Mukta",sans-serif;color:var(--text)}
.abs{position:absolute}
.cond{font-family:"Open Sans Condensed","Open Sans",sans-serif;font-weight:700;text-transform:uppercase}
.script{font-family:"Dancing Script",cursive;font-weight:600}

/* top bar */
.topbar{left:0;top:0;width:1200px;height:25px;background:var(--gold)}
.nav{left:248px;top:0;height:25px;display:flex;align-items:center;gap:18px;font-family:"Open Sans",sans-serif;font-size:11px;color:var(--ink)}
.nav .sep{opacity:.7}
.social-mini{left:848px;top:3px;display:flex;gap:3px}
.social-mini span{width:19px;height:19px;border-radius:50%;background:#fff;opacity:.9;border:2px solid var(--gold-deep)}

/* brand */
.brand{display:flex;align-items:center;gap:10px}
.brand .mark{width:40px;height:40px;border-radius:50%;background:var(--gold)}
.brand .name{font-family:"Open Sans",sans-serif;font-weight:700;font-size:19px;color:var(--gold-deep);letter-spacing:.5px}
.brand-head{left:0;top:25px;width:1200px;height:83px;justify-content:center}

/* hero */
.hero{left:0;top:108px;width:1200px;height:496px;background:radial-gradient(circle at 50% 50%,#f3c9a0 0%,#d98c55 35%,#b8342a 70%,#7a2019 100%)}
.hero-badge{left:457px;top:229px;width:278px;height:278px;border-radius:50%;background:var(--gold);display:flex;flex-direction:column;align-items:center;justify-content:center;color:var(--ink);text-align:center;line-height:1.05}
.hero-badge .l1{font-family:"Open Sans Condensed",sans-serif;font-weight:700;font-size:31px}
.hero-badge .l2{font-family:"Open Sans",sans-serif;font-weight:400;font-size:37px}
.hero-badge .l3{font-family:"Open Sans",sans-serif;font-weight:700;font-size:37px}

/* welcome */
.welcome{left:0;top:604px;width:1200px;height:333px;background:linear-gradient(90deg,#e9e9e9,#f4f4f4 35%,#f4f4f4 65%,#e9e9e9)}
.welcome-head{left:0;top:640px;width:1200px;text-align:center;font-size:18px;color:var(--ink)}
.welcome-script{left:0;top:668px;width:1200px;text-align:center;font-size:36px;color:var(--ink)}
.portrait-hex{left:558px;top:732px;width:84px;height:88px;clip-path:polygon(50% 0,100% 25%,100% 75%,50% 100%,0 75%,0 25%);background:linear-gradient(160deg,#6a7b86,#2d3a44)}
.coach-name{left:0;top:830px;width:1200px;text-align:center;font-size:18px;color:var(--ink)}
.mission{left:360px;top:858px;width:480px;text-align:center;font-size:12px;line-height:17px;color:var(--text)}

/* video */
.video-band{left:0;top:937px;width:1200px;height:325px;background:var(--gold)}
.video-title{left:248px;top:1002px;font-size:19px;color:var(--ink)}
.video-copy{left:248px;top:1040px;width:254px;font-size:11.5px;line-height:16px;color:var(--ink)}
.video-copy p+p{margin-top:16px}
.player{left:522px;top:977px;width:428px;height:248px;border-radius:3px;overflow:hidden;background:linear-gradient(180deg,#f7b14a 0%,#f39a1e 45%,#e4780a 70%,#c7600a 100%);box-shadow:0 6px 10px rgba(0,0,0,.2)}
.player .play{position:absolute;left:188px;top:88px;width:52px;height:52px;border-radius:50%;background:rgba(255,255,255,.9)}
.player .play svg{position:absolute;left:18px;top:14px}
.player .controls{position:absolute;left:0;bottom:0;width:100%;height:26px;background:rgba(40,40,40,.75)}
.player .progress{position:absolute;left:10px;top:5px;width:408px;height:3px;background:rgba(255,255,255,.35)}
.player .progress i{display:block;width:40%;height:100%;background:#fff}
.player .ctrl{position:absolute;top:13px;width:8px;height:8px;background:#ddd}

/* reasons */
.reasons{left:0;top:1262px;width:1200px;height:538px;background:var(--mist)}
.reasons-title{left:0;top:1316px;width:1200px;text-align:center;font-size:18px;color:var(--ink)}
.reasons-script{left:0;top:1342px;width:1200px;text-align:center;font-size:24px;color:var(--ink)}
.timeline{left:0;top:1537px;width:1200px;height:2px;background:#555}
.dot{width:14px;height:14px;border-radius:50%;background:#fff;border:2px solid var(--gold);top:1531px}
.stem{width:1px;background:var(--gold)}
.num{width:44px;height:28px;background:var(--gold);color:#fff;font-family:"Open Sans Condensed",sans-serif;font-weight:700;font-size:24px;line-height:28px;padding-left:6px}
.reason{font-size:11px;line-height:16px;color:var(--text);width:170px}

/* offers */
.offer{top:1800px;width:240px}
.offer .pic{height:255px}
.offer .label{height:46px;display:flex;align-items:center;justify-content:center;text-align:center;font-size:15px;line-height:17px;color:var(--ink);background:var(--mist)}
.offer .label.gold{background:var(--gold)}
.offer .detail{height:50px;padding-top:14px;text-align:center;font-size:11px;line-height:15px;color:var(--text)}
.offer .cta{display:block;margin:0 auto;width:130px;height:32px;border:2px solid var(--gold);text-align:center;line-height:28px;font-family:"Open Sans",sans-serif;font-size:10px;letter-spacing:2px;color:var(--ink);text-decoration:none}

/* stories */
.stories{left:0;top:2258px;width:1200px;height:292px;background:linear-gradient(120deg,#f6b80e,#ffc928 50%,#f1b10a)}
.stories-title{left:0;top:2290px;width:1200px;text-align:center;font-size:19px;color:var(--ink)}
.t-hex{width:74px;height:80px;clip-path:polygon(50% 0,100% 25%,100% 75%,50% 100%,0 75%,0 25%);top:2340px}
.t-name{top:2368px;font-size:12px;color:var(--ink)}
.t-quote{top:2406px;width:230px;font-size:11px;line-height:16px;font-style:italic;color:#fff}
.arrow{top:2414px}
.pager{left:580px;top:2505px;display:flex;gap:7px}
.pager i{width:5px;height:5px;border-radius:50%;background:var(--ink)}
.pager i:first-child{background:#fff}

/* follow */
.follow{left:0;top:2550px;width:1200px;height:167px;background:var(--mist)}
.follow-item{top:2594px;display:flex;align-items:center}
.follow-item .disc{width:70px;height:70px;border-radius:50%;position:relative;z-index:1}
.follow-item .card{margin-left:-8px;height:50px;width:160px;background:#fff;padding:8px 0 0 20px;box-shadow:0 1px 3px rgba(0,0,0,.12)}
.follow-item .card b{display:block;font-family:"Open Sans",sans-serif;font-weight:400;font-size:16px;line-height:19px;color:var(--ink)}
.follow-item .card b em{font-style:normal;color:#1c86c4}
.follow-item .card small{display:block;font-size:9px;line-height:12px;color:var(--muted)}

/* footer */
.footer{left:0;top:2717px;width:1200px;height:180px;background:var(--footer)}
.brand-foot{left:0;top:2757px;width:1200px;justify-content:center}
.copyright{left:0;top:2826px;width:1200px;text-align:center;font-size:10px;color:#d8d8d8}
</style>
</head>
<body>

<header>
  <div class="abs topbar"></div>
  <nav class="abs nav"><span>HOME</span><span class="sep">I</span><span>PRODUCTS</span><span class="sep">I</span><span>BLOGS</span><span class="sep">I</span><span>CONTACT US</span></nav>
  <div class="abs social-mini" aria-label="Social links"><span></span><span></span><span></span><span></span><span></span></div>
  <div class="abs brand brand-head"><span class="mark"></span><span class="name">BRIGHT TURN MENTORING</span></div>
</header>

<section>
  <div class="abs hero" role="img" aria-label="Photo of smiling young people in a circle looking down at the camera"></div>
  <div class="abs hero-badge">
    <span class="l1">BRIGHT TURN</span>
    <span class="l1">IS FUN</span>
    <span class="l2">HAPPY</span>
    <span class="l3">AND</span>
    <span class="l2">INVITING</span>
  </div>
</section>

<section>
  <div class="abs welcome"></div>
  <h2 class="abs welcome-head cond">Welcome to</h2>
  <p class="abs welcome-script script">Bright Turn Mentoring</p>
  <div class="abs portrait-hex" role="img" aria-label="Portrait of Marcus Pellingham"></div>
  <h3 class="abs coach-name cond">Marcus Pellingham</h3>
  <p class="abs mission">My mission is to improve as many people's lives as I can, when I can, through workshops, being guest speaker at events, coaching/mentoring and with valuable products.</p>
</section>

<section>
  <div class="abs video-band"></div>
  <h2 class="abs video-title cond">A Video Bright Turn Mentoring</h2>
  <div class="abs video-copy">
    <p>Lorem Ipsum has been the industry's standard dummy text ever since the 1500s, when an unknown printer took a galley of type and scrambled it to make a type specimen book. It has survived not only five centuries, but also the leap into electronic typesetting, remaining essentially unchanged.</p>
    <p>Lorem Ipsum is simply dummy text of the printing and typesetting industry.</p>
  </div>
  <div class="abs player" role="img" aria-label="Video player showing a golden sunset over the sea">
    <div class="play"><svg width="20" height="24" viewBox="0 0 20 24"><path d="M2 1 L19 12 L2 23 Z" fill="#d8261c"/></svg></div>
    <div class="controls">
      <div class="progress"><i></i></div>
      <span class="ctrl" style="left:12px"></span>
      <span class="ctrl" style="left:28px"></span>
      <span class="ctrl" style="left:386px"></span>
      <span class="ctrl" style="left:404px"></span>
    </div>
  </div>
</section>

<section>
  <div class="abs reasons"></div>
  <h2 class="abs reasons-title cond">Why people choose</h2>
  <p class="abs reasons-script script">'Bright Turn Mentoring'</p>
  <div class="abs timeline"></div>

  <!-- upper reasons -->
  <div class="abs stem" style="left:166px;top:1405px;height:128px"></div>
  <div class="abs num" style="left:166px;top:1405px">01</div>
  <p class="abs reason" style="left:180px;top:1436px">We know how to make Bright Turn in other people's lives. This is our favourite method of making change.</p>

  <div class="abs stem" style="left:373px;top:1465px;height:68px"></div>
  <div class="abs num" style="left:373px;top:1465px">02</div>
  <p class="abs reason" style="left:387px;top:1497px">We give away a lot of FREE stuff.</p>

  <div class="abs stem" style="left:580px;top:1418px;height:115px"></div>
  <div class="abs num" style="left:580px;top:1418px">03</div>
  <p class="abs reason" style="left:594px;top:1449px">We thank you for accepting FREE stuff. We are genuinely grateful for you accepting our FREE stuff.</p>

  <div class="abs stem" style="left:788px;top:1447px;height:86px"></div>
  <div class="abs num" style="left:788px;top:1447px">04</div>
  <p class="abs reason" style="left:802px;top:1478px">We give you a feeling of belonging.</p>

  <div class="abs stem" style="left:995px;top:1428px;height:105px"></div>
  <div class="abs num" style="left:995px;top:1428px">05</div>
  <p class="abs reason" style="left:1009px;top:1459px">We give you the feeling that you are special, because you are.</p>

  <!-- lower reasons -->
  <div class="abs stem" style="left:58px;top:1540px;height:85px"></div>
  <p class="abs reason" style="left:72px;top:1594px">We give you the feeling of significance, because you deserve it.</p>
  <div class="abs num" style="left:58px;top:1625px">06</div>

  <div class="abs stem" style="left:267px;top:1540px;height:66px"></div>
  <p class="abs reason" style="left:281px;top:1566px">We give you the feeling of feeling good.</p>
  <div class="abs num" style="left:267px;top:1606px">07</div>

  <div class="abs stem" style="left:478px;top:1540px;height:66px"></div>
  <p class="abs reason" style="left:492px;top:1566px">We give you positive, empowering experiences.</p>
  <div class="abs num" style="left:478px;top:1606px">08</div>

  <div class="abs stem" style="left:683px;top:1540px;height:174px"></div>
  <p class="abs reason" style="left:697px;top:1624px">We give you tools, models and methodologies to improve every area of your life, continuously for the rest of your life. You can have fulfillment.</p>
  <div class="abs num" style="left:683px;top:1714px">09</div>

  <div class="abs stem" style="left:892px;top:1540px;height:66px"></div>
  <p class="abs reason" style="left:906px;top:1566px">We give you value beyond what you can imagine.</p>
  <div class="abs num" style="left:892px;top:1606px">10</div>

  <span class="abs dot" style="left:51px"></span>
  <span class="abs dot" style="left:159px"></span>
  <span class="abs dot" style="left:260px"></span>
  <span class="abs dot" style="left:366px"></span>
  <span class="abs dot" style="left:471px"></span>
  <span class="abs dot" style="left:573px"></span>
  <span class="abs dot" style="left:676px"></span>
  <span class="abs dot" style="left:781px"></span>
  <span class="abs dot" style="left:885px"></span>
  <span class="abs dot" style="left:988px"></span>
</section>

<section>
  <article class="abs offer" style="left:0">
    <div class="pic" role="img" aria-label="Photo of a thoughtful man under a chalkboard reading mentor" style="background:linear-gradient(180deg,#3a3a3a,#1f1f1f 60%,#6b5a4c)"></div>
    <h3 class="label cond">Personal Coaching /<br>Mentoring</h3>
    <p class="detail">1st Session FREE, valued at A$125,<br>24/7 chat support</p>
    <a class="cta" href="https://bookslotter.example/brightturnmentoring">READ MORE</a>
  </article>
  <article class="abs offer" style="left:240px">
    <div class="pic" role="img" aria-label="Photo of an audience at a seminar" style="background:linear-gradient(180deg,#d9dde0,#9aa3a8 50%,#4b5257)"></div>
    <h3 class="label gold cond">Human Behaviour<br>Events</h3>
    <p class="detail">next upcoming event, call to action<br>button to go to...</p>
    <a class="cta" href="#">READ MORE</a>
  </article>
  <article class="abs offer" style="left:480px">
    <div class="pic" role="img" aria-label="Photo of a hand holding a microphone" style="background:linear-gradient(180deg,#7a6f68,#a89a90 50%,#5b524c)"></div>
    <h3 class="label cond">Guest Speaker / Master<br>of Ceremonies</h3>
    <p class="detail"></p>
    <a class="cta" href="#">CONTACT US</a>
  </article>
  <article class="abs offer" style="left:720px">
    <div class="pic" role="img" aria-label="Chalkboard drawing of a seesaw weighing better and good" style="background:linear-gradient(180deg,#4a4a4a,#2c2c2c)"></div>
    <h3 class="label gold cond">Great Value<br>Products</h3>
    <p class="detail"></p>
    <a class="cta" href="#">PRODUCTS</a>
  </article>
  <article class="abs offer" style="left:960px">
    <div class="pic" role="img" aria-label="Photo of an alpine village church in green mountains" style="background:linear-gradient(180deg,#9fb8c8,#7d9a74 55%,#4f6b3a)"></div>
    <h3 class="label cond">Great Free<br>Information</h3>
    <p class="detail"></p>
    <a class="cta" href="#">BLOGS</a>
  </article>
</section>

<section>
  <div class="abs stories" role="img" aria-label="Gold tinted photo of people working together"></div>
  <h2 class="abs stories-title cond">Success Stories</h2>

  <svg class="abs arrow" style="left:246px" width="14" height="20" viewBox="0 0 14 20"><path d="M11 2 L3 10 L11 18" fill="none" stroke="#222" stroke-width="3"/></svg>
  <svg class="abs arrow" style="left:938px" width="14" height="20" viewBox="0 0 14 20"><path d="M3 2 L11 10 L3 18" fill="none" stroke="#222" stroke-width="3"/></svg>

  <div class="abs t-hex" style="left:276px;background:linear-gradient(160deg,#c9c3bc,#5d5650)" role="img" aria-label="Portrait of Chris"></div>
  <h4 class="abs t-name cond" style="left:364px">Chris</h4>
  <p class="abs t-quote" style="left:354px">Lorem Ipsum has been the industry's standard dummy text ever since the 1500s, when an unknown printer took a galley of type and scrambled it to make a type specimen book.</p>

  <div class="abs t-hex" style="left:642px;background:linear-gradient(160deg,#f1d9b8,#a87a52)" role="img" aria-label="Portrait of James"></div>
  <h4 class="abs t-name cond" style="left:730px">James</h4>
  <p class="abs t-quote" style="left:728px">Lorem Ipsum has been the industry's standard dummy text ever since the 1500s, when an unknown printer took a galley of type and scrambled it to make a type specimen book.</p>

  <div class="abs pager"><i></i><i></i><i></i><i></i></div>
</section>

<section>
  <div class="abs follow"></div>
  <div class="abs follow-item" style="left:242px">
    <span class="disc" style="background:#3b5998"></span>
    <div class="card"><b>We're on <em>Circlebook</em></b><small>Like us to see our daily updates!</small></div>
  </div>
  <div class="abs follow-item" style="left:478px">
    <span class="disc" style="background:#2fa8c9"></span>
    <div class="card"><b>We're on <em>Chirper</em></b><small>Follow us to see our daily updates!</small></div>
  </div>
  <div class="abs follow-item" style="left:716px">
    <span class="disc" style="background:#c1322a"></span>
    <div class="card"><b>We're on <em>Orbitnet</em></b><small>Like us to see our daily updates!</small></div>
  </div>
</section>

<footer>
  <div class="abs footer"></div>
  <div class="abs brand brand-foot"><span class="mark"></span><span class="name">BRIGHT TURN MENTORING</span></div>
  <p class="abs copyright">© 2017 Bright Turn Mentoring, Inc. All rights reserved</p>
</footer>

</body>
</html>
```